Diesel Fitting/Mechanical Company Needs a new Business Card

We would like a new business card that showcases our logo and business information.

Industry/Entity Type

Business

Contact Information for Business Card

314 Wendale Street
PO Box 7581 MERRIVALE DOWNS QLD 4836
Phone: 49312787 Fax: 49312688 Mobile: 0438915276 ABN: 63 519 087 342

Requirements
Must have
• The following email addresses:
• admin@tkservicing.com.au , sales@tkservicing.com.au , accounts@tkservicing.com.au , parts@tkservicing.com.au , office@tkservicing.com.au
• Also need to have the website: www.tkservicing.com.au

```html
<!DOCTYPE html>
<html lang="en">
<head>
<meta charset="utf-8">
<title>TK Servicing – Business Card</title>
<link rel="stylesheet" href="https://fonts.googleapis.com/css2?family=Aleo:wght@300;400;700&display=swap">
<style>
  :root {
    --page-bg: #ffffff;
    --card-black: #060606;
    --brand-orange: #f47a20;
    --text-grey: #b3b5b8;
    --card-shadow: 3px 4px 6px rgba(0, 0, 0, 0.35);
  }
  * { margin: 0; padding: 0; box-sizing: border-box; }
  html, body {
    width: 1200px;
    height: 1000px;
    overflow: hidden;
    background: var(--page-bg);
  }
  .canvas {
    position: relative;
    width: 1200px;
    height: 1000px;
    font-family: "Aleo", Georgia, serif;
  }
  .card {
    position: absolute;
    background: var(--card-black);
    box-shadow: var(--card-shadow);
    overflow: hidden;
  }
  .card--front { left: 344px; top: 52px; width: 515px; height: 334px; }
  .card--back  { left: 342px; top: 406px; width: 517px; height: 334px; }

  /* Front: brand name */
  .brand {
    position: absolute;
    inset: 0;
    display: flex;
    align-items: center;
    justify-content: center;
    gap: 16px;
  }
  .brand__dot {
    width: 26px;
    height: 26px;
    border-radius: 50%;
    background: var(--brand-orange);
  }
  .brand__name {
    font-weight: 700;
    font-size: 40px;
    color: var(--brand-orange);
    letter-spacing: 0.5px;
  }

  /* Back: contact details */
  .contact {
    position: absolute;
    left: 95px;
    top: 107px;
    font-size: 16px;
    line-height: 19.6px;
    color: var(--text-grey);
    font-weight: 300;
    font-style: normal;
    white-space: nowrap;
  }
  .contact__company {
    color: var(--brand-orange);
    font-weight: 700;
  }
  .label {
    color: var(--brand-orange);
    font-weight: 700;
  }
  .gap { margin-left: 8px; }

  .emails {
    position: absolute;
    left: 95px;
    top: 217px;
    font-size: 14.6px;
    line-height: 18.2px;
    color: var(--text-grey);
    font-weight: 300;
    list-style: none;
    white-space: nowrap;
  }
  .emails__user { color: var(--brand-orange); font-weight: 700; }
  .emails li:nth-child(2) { padding-left: 3px; }
  .emails li:nth-child(3) { padding-left: 7px; }
  .emails li:nth-child(4) { padding-left: 18px; }
  .emails li:nth-child(5) { padding-left: 29px; }

  .website {
    position: absolute;
    left: 443px;
    top: 103px;
    writing-mode: vertical-rl;
    font-size: 16.6px;
    letter-spacing: 0.8px;
    color: var(--brand-orange);
    font-weight: 400;
    white-space: nowrap;
  }
</style>
</head>
<body>
<main class="canvas">
  <section class="card card--front" aria-label="Business card front">
    <div class="brand">
      <span class="brand__dot" aria-hidden="true"></span>
      <span class="brand__name">TK Servicing</span>
    </div>
  </section>

  <section class="card card--back" aria-label="Business card back">
    <address class="contact">
      <div class="contact__company">TK Servicing</div>
      <div>314 Wendale Street</div>
      <div>PO Box 7581 Merrivale Downs QLD 4836</div>
      <div><span class="label">T:</span> 49312787<span class="gap"></span><span class="label">F:</span> 49312688</div>
      <div><span class="label">M:</span> 0438915276<span class="gap"></span><span class="label">ABN:</span> 63 519 087 342</div>
    </address>

    <ul class="emails">
      <li><span class="emails__user">admin</span>@tkservicing.com.au</li>
      <li><span class="emails__user">sales</span>@tkservicing.com.au</li>
      <li><span class="emails__user">accounts</span>@tkservicing.com.au</li>
      <li><span class="emails__user">parts</span>@tkservicing.com.au</li>
      <li><span class="emails__user">office</span>@tkservicing.com.au</li>
    </ul>

    <div class="website">www.tkservicing.com.au</div>
  </section>
</main>
</body>
</html>
```